Diet, Exercise, & Friends are Associated with Parkinson's disease Progression

We are researchers looking for modifiable variables associated with different rates of Parkinson's disease (PD) progression. This is a novel scale: www.VELQAN.org -- higher scores are associated with worse quality of life. Low is good. High is bad. Each of the dots is a real person (maybe those should disappear?). The line represents the typical rate of PD progression over time. Color scheme of different degrees of quality of life can change, but the general concept seems to be working. (see updated version at the bottom of the www.VELQAN.org website)We need to combine the exercise data from here. This poster was essentially my attempt at an infographic for scientists:https://files.brindlehost.net/static/7a2c91e0b4/t/3d8e55f1a0/1482209931245/TRX2017+Meals.pdf. The updated data is in the uploaded figure below. Please use this list/ verbage!I don't necessarily need to stick to red=bad, green=good, but that's the best I've been able to come up with to communicate all this. I can get the actual data output later, but it might be nice to be able to demonstrate intensity. Veggies are quite a bit better than spices. Loneliness is much, much worse than pasta. This is the original published data. We have updated data and want to turn it into an infographic (while we work on a new manuscript).https://www.quorvelpress.com/journals/jcrt/2017/8127439/
Target Market(s)
Individuals age 40-80 with Parkinson's disease (and their friends & family members).
Neurologists should be handing this out in their offices.
When patients ask their physician about nutrition, etc., we want this to be the 1-pg handout they give them.
Industry/Entity Type
Medicine
Font styles to use
Colors
Designer to choose colors to be used in the design.
Requirements
Must have
- VEL-QAN scale (www.VELQAN.org)-- use this picture on top. OK to change color.
- Lists foods/ activities associated with different rates of progression
- Title: "Food, Friends, and Exercise: Lifestyle Associations with PD Progression"
- Legend/ disclaimer (smaller font):
- "All results were adjusted for age, gender, and years since diagnosis. Total sample size: 1600+
- Based on the methods described in publication: "Effects of Meal Timing and Herbal Intake on Tremor Course" [Orvanto TJ et al, Clin Neuro Rehab Rev 2017], an updated analysis was performed on data on 7 May 2019. (N >1600)"
- "VEL-QAN scores available at www.VELQAN.org"
- Must fit on a single 8.5 x 11" page.
Nice to have
- The background should be white-- I want neurologists/ physicians downloading it, printing it, and distributing to patients. I don't want to waste ink.
- Logo for Kellworth University and/or the logo for the "HOLT Path MX" Study. I like the KU emblem in one corner and the picture at the top of this website: www.VELQAN.org
- Would be nice if it could be understood between cultures and/ or easily translated.
- Would be nice if we could invite people to participate in the study!
- "To learn about joining the study, please to www.HOLTPathMX.kellworth.edu"
Should not have
- Pictures of overweight people, or the impression that a muscular white guy is the ideal. I want to leave room for diversity and flexible interpretation.
- Too much text- a good-sized portion of this group will have poor vision and/or dementia. Needs to be simple.
- I like the simplicity of "Good" and "Bad"... don't love the labels. Seems to 'jugdgy'. Maybe "Encourage" and "Avoid" OR "Positive" and "Negative"

```html
<!DOCTYPE html>
<html lang="en">
<head>
<meta charset="utf-8">
<title>Food, Friends and Exercise: Lifestyle Associations with Parkinson's Disease Progression</title>
<link rel="stylesheet" href="https://fonts.googleapis.com/css2?family=Mada:wght@300;400;500;700;900&display=swap">
<style>
  :root{
    --teal-dark:#1c8a93;
    --teal:#2aa3ad;
    --excellent:#6cc9d6;
    --good:#cdf2f4;
    --fair:#f8bf98;
    --avoid:#fd7d35;
    --orange-text:#f26a21;
    --brown-text:#8a3c1a;
    --band:#c6f0f2;
    --maroon:#8a2b1e;
    --page:#ffffff;
  }
  *{margin:0;padding:0;box-sizing:border-box}
  html,body{width:1200px;height:1200px;overflow:hidden;background:var(--page)}
  body{position:relative;font-family:"Mada",sans-serif;color:var(--teal-dark)}
  .poster{position:absolute;left:213px;top:109px;width:768px;height:995px;
    background:linear-gradient(180deg,#d3f4f5 0%,#f5fdfd 30%,#ffffff 36%,#ffffff 50%,#e2f8f9 100%);
    box-shadow:0 2px 6px rgba(0,0,0,.18)}
  .poster-band{position:absolute;left:213px;top:452px;width:768px;height:6px;background:var(--band)}
  .abs{position:absolute}
  .title{left:268px;top:143px;font-size:28px;font-weight:900;letter-spacing:.5px;color:var(--teal-dark);white-space:nowrap}
  .subtitle{left:268px;top:176px;font-size:18.5px;font-weight:300;color:var(--teal);white-space:nowrap}
  .brand{left:740px;top:160px;width:132px;text-align:right;font-size:11px;font-weight:700;color:var(--teal-dark);line-height:1.15}
  .brand-mark{left:880px;top:142px;width:58px;height:58px;border-radius:50%;background:var(--maroon)}
  .intro-head{left:270px;top:222px;width:250px;font-size:11.5px;font-weight:700;color:var(--orange-text);line-height:1.2}
  .intro-body{left:270px;top:263px;width:262px;font-size:12.3px;font-weight:500;color:var(--teal-dark);line-height:1.12}
  .intro-note{left:270px;top:317px;width:250px;font-size:7.4px;color:var(--teal);line-height:1.2}
  .intro-cite{left:270px;top:345px;width:262px;font-size:7.4px;font-style:italic;color:var(--teal);line-height:1.2}
  .col-rule{left:551px;top:225px;width:1px;height:208px;background:var(--band)}
  .chart{left:560px;top:215px}
  .result-head{left:270px;top:479px;font-size:18px;font-weight:900;color:var(--teal-dark)}
  .result-sub{left:270px;top:504px;width:600px;font-size:13.2px;font-weight:300;color:var(--teal);line-height:1.15}
  .curve{left:340px;top:540px}
  .figure{position:absolute;border-radius:14px}
  .col-label{position:absolute;top:670px;width:130px;text-align:center;font-size:9px;font-weight:700;letter-spacing:.3px}
  .cell{position:absolute;padding:21px 10px 0 17px;font-size:10px;font-weight:700;line-height:11.8px}
  .excellent{background:var(--excellent);color:#fff}
  .good{background:var(--good);color:var(--teal-dark)}
  .fair{background:var(--fair);color:var(--brown-text)}
  .avoid{background:var(--avoid);color:#fff}
  .row-icon{position:absolute;left:278px;width:48px;height:48px;border-radius:50%;
    background:radial-gradient(circle at 40% 35%,#4fb8c2,#1c7d86);box-shadow:0 1px 3px rgba(0,0,0,.25)}
  .row-label{position:absolute;left:262px;width:80px;text-align:center;font-size:9.5px;font-weight:700;color:var(--teal)}
  .study-mark{left:580px;top:1024px;width:34px;height:34px;border-radius:50%;border:3px solid #3b4ea0;background:#cfe4f6}
  .footer{left:213px;top:1067px;width:768px;text-align:center;font-size:8px;font-style:italic;color:var(--teal-dark)}
</style>
</head>
<body>
  <div class="poster"></div>
  <div class="poster-band"></div>

  <header>
    <h1 class="abs title">FOOD, FRIENDS AND EXERCISE :</h1>
    <p class="abs subtitle">Lifestyle Associations with Parkinson’s Disease Progression</p>
    <p class="abs brand">Kellworth University</p>
    <div class="abs brand-mark"></div>
  </header>

  <section class="intro">
    <h2 class="abs intro-head">THE PATIENT REPORTED OUTCOME GRAPH REPORTS</h2>
    <p class="abs intro-body">The corelation of the quantity of dietary and supplements intake and the activities/lifestyle of a patient with the patient’s quality of life.</p>
    <p class="abs intro-note">All results adjusted for age, gender, and years since diagnosis.<br>Total sample size: 1600+.</p>
    <p class="abs intro-cite">Based on the methods described in publication:<br>“Effects of Meal Timing and Herbal Intake on Tremor Course”<br>(Orvanto TJ et al, Clin Neuro Rehab Rev 2017),<br>an updated analysis was performed on data on 7 May 2019.<br>(N &gt;1600)</p>
  </section>

  <div class="abs col-rule"></div>

  <svg class="abs chart" width="420" height="225" viewBox="560 215 420 225" font-family="Mada, sans-serif">
    <text x="573" y="232" font-size="9" font-weight="700" fill="#1c8a93">Patient-Reported Outcomes in Parkinson Disease</text>
    <defs>
      <linearGradient id="poorFill" x1="0" y1="0" x2="0" y2="1">
        <stop offset="0" stop-color="#e0682a"/><stop offset="1" stop-color="#f7884a"/>
      </linearGradient>
    </defs>
    <rect x="626" y="250" width="240" height="52" fill="url(#poorFill)"/>
    <rect x="626" y="302" width="240" height="24" fill="#f8bf98"/>
    <rect x="626" y="326" width="240" height="26" fill="#b9e4ea"/>
    <rect x="626" y="352" width="240" height="30" fill="#6cc9d6"/>
    <polygon points="626,340 866,281 866,303" fill="#fde3cf" opacity=".85"/>
    <line x1="626" y1="340" x2="866" y2="293" stroke="#f26a21" stroke-width="1.4"/>
    <g font-size="6.5" fill="#555" text-anchor="end">
      <text x="605" y="252">2500</text><text x="605" y="277">2000</text>
      <text x="605" y="303">1500</text><text x="605" y="328">1000</text>
      <text x="605" y="353">500</text><text x="602" y="377">0</text>
    </g>
    <g stroke="#9dd7dc" stroke-width=".8">
      <line x1="612" y1="250" x2="618" y2="250"/><line x1="612" y1="275" x2="618" y2="275"/>
      <line x1="612" y1="301" x2="618" y2="301"/><line x1="612" y1="326" x2="618" y2="326"/>
      <line x1="612" y1="351" x2="618" y2="351"/><line x1="612" y1="375" x2="618" y2="375"/>
      <line x1="629" y1="389" x2="629" y2="395"/><line x1="676" y1="389" x2="676" y2="395"/>
      <line x1="723" y1="389" x2="723" y2="395"/><line x1="770" y1="389" x2="770" y2="395"/>
      <line x1="818" y1="389" x2="818" y2="395"/><line x1="865" y1="389" x2="865" y2="395"/>
    </g>
    <g font-size="6.5" fill="#555" text-anchor="middle">
      <text x="629" y="409">0</text><text x="676" y="409">5</text><text x="723" y="409">10</text>
      <text x="770" y="409">15</text><text x="818" y="409">20</text><text x="865" y="409">25</text>
    </g>
    <text x="743" y="429" font-size="7.5" fill="#f26a21" text-anchor="middle">number of years since diagnosis</text>
    <text transform="translate(574,289) rotate(90)" font-size="7" fill="#f26a21">PD severity</text>
    <text x="884" y="256" font-size="8" font-weight="700" fill="#2aa3ad">Quality of life</text>
    <rect x="884" y="264" width="9" height="9" fill="#f26a21"/><text x="899" y="271" font-size="7" font-weight="700" fill="#f26a21">Poor</text>
    <rect x="884" y="278" width="9" height="9" fill="#f8bf98"/><text x="899" y="285" font-size="7" fill="#f8bf98">Fair</text>
    <rect x="884" y="292" width="9" height="9" fill="#b9e4ea"/><text x="899" y="299" font-size="7" fill="#9ad3dc">Good</text>
    <rect x="884" y="307" width="9" height="9" fill="#4fb8c4"/><text x="899" y="314" font-size="7" font-weight="700" fill="#2aa3ad">Excellent</text>
    <g font-size="6" font-style="italic" fill="#2aa3ad">
      <text x="883" y="336">VEL-QAN scores</text>
      <text x="883" y="343">available at</text>
      <text x="883" y="350">www.VELQAN.org</text>
    </g>
  </svg>

  <section class="result">
    <h2 class="abs result-head">THE RESULT</h2>
    <p class="abs result-sub">The result shows some food, supplement and activites improves the outcome of progression,<br>while some worsen the outcome.</p>

    <svg class="abs curve" width="560" height="130" viewBox="340 540 560 130">
      <defs>
        <clipPath id="cExcellent"><rect x="358" y="540" width="130" height="130"/></clipPath>
        <clipPath id="cGood"><rect x="491" y="540" width="131" height="130"/></clipPath>
        <clipPath id="cFair"><rect x="624" y="540" width="130" height="130"/></clipPath>
        <clipPath id="cAvoid"><rect x="757" y="540" width="131" height="130"/></clipPath>
        <path id="bell" d="M358,664 C420,662 455,650 488,632 C540,602 575,546 622,546 C670,546 705,602 756,632 C790,650 825,662 888,664 Z"/>
      </defs>
      <use href="#bell" fill="#6cc9d6" clip-path="url(#cExcellent)"/>
      <use href="#bell" fill="#cdf2f4" clip-path="url(#cGood)"/>
      <use href="#bell" fill="#f8bf98" clip-path="url(#cFair)"/>
      <use href="#bell" fill="#fd7d35" clip-path="url(#cAvoid)"/>
    </svg>

    <div class="figure" role="img" aria-label="Person walking briskly" style="left:350px;top:592px;width:34px;height:64px;background:#6cc9d6"></div>
    <div class="figure" role="img" aria-label="Person walking" style="left:472px;top:557px;width:30px;height:63px;background:#cdf2f4"></div>
    <div class="figure" role="img" aria-label="Person walking with a cane" style="left:740px;top:557px;width:33px;height:63px;background:#f8bf98"></div>
    <div class="figure" role="img" aria-label="Person in a wheelchair" style="left:850px;top:597px;width:51px;height:59px;background:#fd7d35"></div>

    <span class="col-label" style="left:358px;color:#2aa3ad">EXCELLENT</span>
    <span class="col-label" style="left:491px;color:#9ad3dc">GOOD</span>
    <span class="col-label" style="left:624px;color:#f5a77a">FAIR</span>
    <span class="col-label" style="left:757px;color:#f26a21">AVOID</span>

    <div class="row-icon" style="top:717px" role="img" aria-label="Apple icon">
      <svg width="48" height="48" viewBox="0 0 48 48"><path d="M24 17c-3-2-8-1-9 4-1 5 3 12 6 12 1.5 0 2-.8 3-.8s1.5.8 3 .8c3 0 7-7 6-12-1-5-6-6-9-4z M24 17c0-3 1-5 3-6" fill="none" stroke="#d6f4f6" stroke-width="1.4"/></svg>
    </div>
    <span class="row-label" style="top:774px">FOOD</span>

    <div class="row-icon" style="top:814px" role="img" aria-label="Exercise icon">
      <svg width="48" height="48" viewBox="0 0 48 48"><circle cx="24" cy="24" r="12" fill="none" stroke="#d6f4f6" stroke-width="1.2"/></svg>
    </div>
    <span class="row-label" style="top:871px">EXERCISE</span>

    <div class="row-icon" style="top:916px" role="img" aria-label="Hexagon cluster icon">
      <svg width="48" height="48" viewBox="0 0 48 48" fill="none" stroke="#d6f4f6" stroke-width="1.3">
        <polygon points="18,14 23,14 25.5,18.5 23,23 18,23 15.5,18.5"/>
        <polygon points="26,18.5 31,18.5 33.5,23 31,27.5 26,27.5 23.5,23"/>
        <polygon points="18,23.5 23,23.5 25.5,28 23,32.5 18,32.5 15.5,28"/>
      </svg>
    </div>
    <span class="row-label" style="top:971px">LIFESTYLE</span>

    <div class="cell excellent" style="left:358px;top:689px;width:130px;height:110px">Fresh vegetables<br>Fresh Fruit<br>Nuts &amp; seeds<br>Non-fried fish</div>
    <div class="cell good" style="left:491px;top:689px;width:131px;height:110px">Olive &amp; coconut&nbsp; oil<br>Fresh herbs<br>Spices</div>
    <div class="cell fair" style="left:624px;top:689px;width:130px;height:110px;padding-left:35px">Wine<br>Dairy<br>Beef<br>Chicken</div>
    <div class="cell avoid" style="left:757px;top:689px;width:131px;height:110px;padding-left:21px">Fried foods<br>Soda<br>Canned fruits<br>Canned vegetables<br>Frozen vegetables</div>

    <div class="cell excellent" style="left:358px;top:802px;width:130px;height:90px;padding-top:31px">7 days/week<br>6 days/week</div>
    <div class="cell good" style="left:491px;top:802px;width:131px;height:90px;padding-top:31px">5 days/week<br>4 days/week</div>
    <div class="cell fair" style="left:624px;top:802px;width:130px;height:90px;padding-top:31px;padding-left:35px">3 days/week</div>
    <div class="cell avoid" style="left:757px;top:802px;width:131px;height:90px;padding-top:31px;padding-left:21px">2 - 0 days/week</div>

    <div class="cell excellent" style="left:358px;top:896px;width:130px;height:102px">I try to eat organic<br>when possible<br>I have a lot of friends</div>
    <div class="cell good" style="left:491px;top:896px;width:131px;height:102px">I cook most<br>of my own meals</div>
    <div class="cell fair" style="left:624px;top:896px;width:130px;height:102px;padding-left:35px">I am lonely</div>
    <div class="cell avoid" style="left:757px;top:896px;width:131px;height:102px;padding-left:21px">I am overweight</div>
  </section>

  <footer>
    <div class="abs study-mark"></div>
    <p class="abs footer">For information about joining this study, please visit www.HOLTPathMX.kellworth.edu</p>
  </footer>
</body>
</html>
```